Design My Bussiness Card
Technology company
Project: Design My Bussiness Card
Design My Bussiness Card -
Creative Brief
Professional
Dorian Pelkey
2847 E. Tollbrook #3
marisa@vantrelo.net
www.qoribelix.info

```html
<!DOCTYPE html>
<html lang="en">
<head>
<meta charset="utf-8">
<title>Qoribelix Stationery Set</title>
<link href="https://fonts.googleapis.com/css2?family=Tinos:wght@400;700&display=swap" rel="stylesheet">
<style>
  :root {
    --green: #2f9a3f;
    --green-faint: #e6f2e5;
    --brown: #3c2a1e;
    --ink: #4a4a4a;
    --paper: #ffffff;
    --edge: #d9d9d9;
    --backdrop: #ffffff;
  }
  html, body {
    margin: 0;
    padding: 0;
    width: 1200px;
    height: 1101px;
    overflow: hidden;
    background: var(--backdrop);
    font-family: "Tinos", "Times New Roman", serif;
    color: var(--ink);
  }
  .stationery { position: relative; width: 1200px; height: 1101px; }
  .sheet {
    position: absolute;
    background: var(--paper);
    border: 1px solid var(--edge);
    box-shadow: 0 2px 6px rgba(0,0,0,0.12);
    overflow: hidden;
    box-sizing: border-box;
  }
  .brand { position: absolute; }
  .brand-row { display: flex; align-items: center; gap: 10px; }
  .brand-dot { border-radius: 50%; background: var(--green); flex: none; }
  .brand-name { font-weight: 700; color: var(--green); letter-spacing: 0.5px; line-height: 1; }
  .brand-tagline { color: var(--green); text-transform: uppercase; letter-spacing: 0.6px; margin-top: 3px; white-space: nowrap; }
  .faint-ring { position: absolute; border-radius: 50%; border-style: solid; border-color: var(--green-faint); }

  /* Letterhead */
  .letterhead { left: 36px; top: 36px; width: 723px; height: 1029px; }
  .letterhead .brand { left: 36px; top: 42px; }
  .letterhead .brand-dot { width: 30px; height: 30px; }
  .letterhead .brand-name { font-size: 34px; }
  .letterhead .brand-tagline { font-size: 11px; padding-left: 40px; }
  .letterhead .faint-ring { left: -70px; top: 690px; width: 330px; height: 330px; border-width: 44px; }
  .letterhead-footer {
    position: absolute; left: 369px; top: 970px;
    font-size: 12px; line-height: 18px; color: var(--ink); white-space: nowrap;
  }
  .letterhead-footer .web { color: var(--green); font-weight: 700; }

  /* Business card */
  .card-front { left: 861px; top: 36px; width: 309px; height: 198px; }
  .card-front .brand { left: 14px; top: 16px; }
  .card-front .brand-dot { width: 16px; height: 16px; }
  .card-front .brand-row { gap: 6px; }
  .card-front .brand-name { font-size: 19px; }
  .card-front .brand-tagline { font-size: 6px; padding-left: 22px; }
  .card-front .faint-ring { left: -34px; top: 66px; width: 100px; height: 100px; border-width: 15px; }
  .card-contact {
    position: absolute; left: 186px; top: 108px;
    font-size: 7.5px; line-height: 11px; white-space: nowrap;
  }
  .card-contact .person { font-size: 11px; font-weight: 700; color: var(--ink); margin-bottom: 4px; }
  .card-contact .web { color: var(--green); }

  .card-back {
    left: 861px; top: 240px; width: 309px; height: 210px;
    background: var(--brown); border-color: var(--brown);
    display: flex; align-items: center; justify-content: center; gap: 10px;
  }
  .card-back .brand-dot { width: 18px; height: 18px; background: var(--paper); }
  .card-back .brand-name { color: var(--paper); font-size: 22px; }

  /* Envelope */
  .envelope { position: absolute; left: 369px; top: 456px; width: 801px; height: 498px; }
  .envelope svg { position: absolute; left: 0; top: 0; }
  .envelope .brand { left: 36px; top: 196px; }
  .envelope .brand-dot { width: 28px; height: 28px; }
  .envelope .brand-name { font-size: 32px; }
  .envelope .brand-tagline { font-size: 10px; padding-left: 38px; }
  .envelope .return-address { position: absolute; right: 36px; bottom: 36px; font-size: 11px; white-space: nowrap; }
</style>
</head>
<body>
<main class="stationery">

  <section class="sheet letterhead" aria-label="Letterhead">
    <div class="brand">
      <div class="brand-row"><span class="brand-dot"></span><span class="brand-name">Qoribelix</span></div>
      <div class="brand-tagline">Professional Business Services</div>
    </div>
    <div class="faint-ring" aria-hidden="true"></div>
    <div class="letterhead-footer">
      2847 E. Tollbrook #3 &nbsp;T: 555-014-2280<br>
      F: 555-014-2281 &nbsp;E: marisa@vantrelo.net &nbsp;<span class="web">www.qoribelix.info</span>
    </div>
  </section>

  <section class="sheet card-front" aria-label="Business card front">
    <div class="faint-ring" aria-hidden="true"></div>
    <div class="brand">
      <div class="brand-row"><span class="brand-dot"></span><span class="brand-name">Qoribelix</span></div>
      <div class="brand-tagline">Professional Business Services</div>
    </div>
    <div class="card-contact">
      <div class="person">Dorian Pelkey</div>
      2847 E. Tollbrook #3<br>
      T: 555-014-2280 &nbsp;F: 555-014-2281<br>
      marisa@vantrelo.net<br>
      <span class="web">www.qoribelix.info</span>
    </div>
  </section>

  <section class="sheet card-back" aria-label="Business card back">
    <span class="brand-dot"></span><span class="brand-name">Qoribelix</span>
  </section>

  <section class="envelope" aria-label="Envelope">
    <svg width="801" height="498" viewBox="0 0 801 498">
      <rect x="0.5" y="150" width="800" height="347.5" fill="#ffffff" stroke="#d9d9d9"/>
      <path d="M0 150 L0 132 Q0 118 22 112 L290 22 Q400 -6 511 22 L779 112 Q801 118 801 132 L801 150 Z" fill="#3c2a1e"/>
      <circle cx="400.5" cy="84" r="19" fill="#ffffff"/>
    </svg>
    <div class="brand">
      <div class="brand-row"><span class="brand-dot"></span><span class="brand-name">Qoribelix</span></div>
      <div class="brand-tagline">Professional Business Services</div>
    </div>
    <div class="return-address">2847 E. Tollbrook #3</div>
  </section>

</main>
</body>
</html>
```